Company Website Re-design for Software development consultancy

We would like our company website to be redesigned using our existing marketing collateral and website content as a guide

current site : www.brackenloft.com.au

For the different pages types and content please base on the following site : https://www.quorvanta.net/

We want a coded site - but will replace the content ourselves within the sections you provide to customise to our needs.

Target Market(s)

Medium to Large corporates needing software design and development services

Industry/Entity Type

Information Technology

Coding

Coded - Design and coding required

Number of Pages Required

5+ page

Font styles to use
Sans Serif

Colors
ec1f27
ffffff
000000

Requirements
Must have
• Align to colour scheme of existing collateral
• Include pages for the key areas of our busines - see : https://www.quorvanta.net/
Nice to have
• image rotators - make the site interesting to the business visitor

```html
<!DOCTYPE html>
<html lang="en">
<head>
<meta charset="utf-8">
<title>Bracken Loft — Software Development</title>
<link href="https://fonts.googleapis.com/css2?family=Oswald:wght@400;500;700&family=Open+Sans:wght@400;600&display=swap" rel="stylesheet">
<style>
:root{
  --red:#ec1f27;
  --white:#ffffff;
  --black:#000000;
  --ink:#222222;
  --muted:#555555;
  --line:#e3e3e3;
  --dark:#1b1b1b;
  --bar:#2a2a2a;
  --social:#2f6fc0;
}
*{box-sizing:border-box;margin:0;padding:0}
html,body{width:1200px;height:4045px;overflow:hidden}
body{font-family:"Open Sans",Arial,sans-serif;color:var(--ink);background:var(--white);font-size:13px;line-height:1.55}
.head{font-family:"Oswald",Arial,sans-serif;text-transform:uppercase}
.wrap{position:relative;width:1200px}
.abs{position:absolute}
.accent{color:var(--red)}
.btn{display:inline-block;font-family:"Oswald",Arial,sans-serif;text-transform:uppercase;font-size:14px;border-radius:18px;text-align:center}
.btn-red{background:var(--red);color:var(--white)}
.section-title{text-align:center;font-family:"Oswald",Arial,sans-serif;font-size:32px;font-weight:700;text-transform:uppercase;color:var(--black)}
.section-title::after{content:"";display:block;width:90px;height:2px;background:var(--red);margin:10px auto 0}
.section-intro{width:640px;margin:0 auto;text-align:center;color:var(--muted);font-size:13px}

/* header */
.site-header{height:113px}
.logo{left:173px;top:42px;font-family:"Oswald",sans-serif;font-weight:700;font-size:40px;line-height:1;color:var(--black);letter-spacing:1px}
.top-social{right:173px;top:8px;display:flex;gap:4px}
.top-social span{width:20px;height:20px;background:var(--social);display:block}
.nav{left:585px;top:54px;display:flex;gap:0}
.nav a{font-family:"Oswald",sans-serif;font-size:13px;text-transform:uppercase;color:var(--black);text-decoration:none;height:32px;line-height:30px;padding:0 14px;border:2px solid transparent;margin-right:34px}
.nav a.active{border-color:var(--red);color:var(--red)}

/* hero */
.hero{top:113px;height:513px;width:1200px;background:linear-gradient(100deg,#3c3b3a 0%,#6b6563 30%,#a39690 55%,#8a7b72 75%,#5a5550 100%)}
.hero-title{left:173px;top:200px;font-family:"Oswald",sans-serif;font-weight:700;font-size:48px;color:var(--white);line-height:1}
.hero-sub{left:173px;top:258px;font-family:"Oswald",sans-serif;font-size:15px;color:var(--white);text-transform:uppercase;letter-spacing:.5px}
.hero-btn{left:173px;top:320px;width:130px;height:34px;line-height:34px;background:var(--black);color:var(--white)}
.arrow{top:228px;width:40px;height:40px;border-radius:50%;background:rgba(0,0,0,.45)}
.arrow svg{display:block;margin:12px auto}

/* about */
.about{top:626px;height:480px}
.about-photo{left:0;top:0;width:599px;height:480px;background:linear-gradient(135deg,#c74449,#e2585c 50%,#b83a3f)}
.about-frame{left:108px;top:29px;width:447px;height:418px;border:2px solid rgba(255,255,255,.85)}
.about-title{left:663px;top:40px;font-size:30px;font-weight:700;color:var(--black)}
.about-sub{left:663px;top:110px;font-family:"Oswald",sans-serif;font-size:16px;font-weight:500;text-transform:uppercase;color:var(--black)}
.about-text{left:663px;top:144px;width:370px;color:var(--muted);font-size:12px;line-height:1.6}
.checks{left:663px;top:272px;list-style:none;font-size:12px;color:var(--muted)}
.checks li{display:flex;align-items:center;gap:10px;height:24px}
.checks i{width:12px;height:12px;background:var(--red);display:block;position:relative}
.checks i::after{content:"";position:absolute;left:3px;top:1px;width:4px;height:7px;border:solid #fff;border-width:0 2px 2px 0;transform:rotate(45deg)}
.about-btn{left:663px;top:391px;width:130px;height:33px;line-height:33px}

/* services */
.services{top:1106px;height:790px;background:#fafafa}
.services .section-title{padding-top:64px}
.services .section-intro{margin-top:18px}
.service-grid{left:173px;top:210px;width:854px;height:464px;display:grid;grid-template-columns:repeat(3,1fr);grid-template-rows:repeat(2,1fr);background:var(--white);border:1px solid var(--line)}
.service{border-right:1px solid var(--line);border-bottom:1px solid var(--line);text-align:center;padding:22px 26px 0}
.service:nth-child(3n){border-right:none}
.service:nth-child(n+4){border-bottom:none}
.service-icon{width:56px;height:56px;border:2px solid var(--red);border-radius:50%;margin:0 auto 20px;display:flex;align-items:center;justify-content:center}
.service h3{font-family:"Oswald",sans-serif;font-size:15px;font-weight:500;text-transform:uppercase;color:var(--black);margin-bottom:10px}
.service p{font-size:11.5px;color:var(--muted);line-height:1.6}
.services-btn{left:533px;top:712px;width:134px;height:34px;line-height:34px}

/* stats */
.stats{top:1896px;height:140px;background:linear-gradient(90deg,#111 0%,#2b2b2b 45%,#1a1a1a 100%);color:var(--white)}
.stat{top:20px;width:200px;text-align:center;margin-left:-100px}
.stat strong{display:block;font-family:"Oswald",sans-serif;font-size:28px;font-weight:500;line-height:1.1;margin-top:6px}
.stat span{font-size:13px}

/* projects */
.projects{top:2036px;height:712px}
.projects .section-title{padding-top:64px}
.projects .section-intro{margin-top:18px}
.filters{left:380px;top:196px;display:flex;gap:4px}
.filters span{width:101px;height:32px;line-height:30px;text-align:center;border:1px solid #cfcfcf;font-size:12px;color:var(--ink)}
.filters span.on{background:var(--red);border-color:var(--red);color:var(--white)}
.project-grid{left:0;top:259px;width:1200px;height:453px;display:grid;grid-template-columns:repeat(4,1fr);grid-template-rows:repeat(2,1fr)}
.shot-1{background:linear-gradient(135deg,#cfc6bd,#8e8279)}
.shot-2{background:linear-gradient(135deg,#f1f1f1,#c9c9cc)}
.shot-3{background:linear-gradient(135deg,#7d7d7d,#4a4a4a)}
.shot-4{background:linear-gradient(135deg,#f4f4f4,#d6d6d6)}
.shot-5{background:linear-gradient(135deg,#e8eef4,#8fb5d4)}
.shot-6{background:linear-gradient(135deg,#f0f0f0,#e0b94a)}
.shot-7{background:linear-gradient(135deg,#fafafa,#d5d8dc)}
.shot-8{background:linear-gradient(135deg,#e9eef5,#6b8fb8)}

/* team */
.team{top:2748px;height:456px}
.team .section-title{padding-top:46px}
.team .section-intro{margin-top:18px}
.team-box{left:173px;top:176px;width:854px;height:237px;background:var(--black);display:grid;grid-template-columns:repeat(4,1fr);padding:14px 0}
.member{text-align:center;color:var(--white);border-right:1px solid #333}
.member:last-child{border-right:none}
.avatar{width:90px;height:90px;border-radius:50%;border:3px solid var(--white);background:linear-gradient(135deg,#bfbfbf,#7a7a7a);margin:0 auto 16px}
.member h4{font-family:"Oswald",sans-serif;font-size:15px;font-weight:500;text-transform:uppercase}
.member p{font-size:11px;margin-bottom:10px}
.member-social{display:flex;gap:4px;justify-content:center}
.member-social span{width:20px;height:20px;background:var(--white);display:block}

/* testimonials */
.testimonials{top:3204px;height:297px;background:linear-gradient(180deg,#e8575c,#f07f83)}
.testi-title{left:173px;top:20px;font-size:28px;font-weight:700;color:var(--white)}
.testi-title::after{content:"";display:block;width:60px;height:2px;background:var(--white);margin-top:6px}
.quote-box{left:173px;top:102px;width:854px;height:104px;border:1px solid rgba(255,255,255,.8);padding:18px 26px 0 58px;color:var(--white);font-size:11.5px;line-height:1.6}
.quote-mark{left:190px;top:118px}
.testi-avatar{left:245px;top:186px;width:82px;height:74px;background:linear-gradient(135deg,#d9b6a4,#8a6a5c);border:2px solid var(--white)}
.testi-name{left:345px;top:216px;color:var(--white)}
.testi-name h5{font-family:"Oswald",sans-serif;font-size:13px;font-weight:500;text-transform:uppercase;line-height:1.2}
.testi-name p{font-size:11px;text-transform:uppercase}
.dots{left:990px;top:228px;display:flex;gap:5px}
.dots span{width:9px;height:9px;background:var(--white)}

/* footer */
.footer{top:3501px;height:496px;background:var(--black);color:var(--white)}
.contact-bar{left:173px;top:51px;width:854px;height:81px;background:var(--bar);display:grid;grid-template-columns:repeat(3,1fr);align-items:center;padding:0 26px}
.contact-item{display:flex;align-items:center;gap:16px}
.contact-icon{width:48px;height:48px;border:1px solid #777;display:flex;align-items:center;justify-content:center}
.contact-item h6{font-family:"Oswald",sans-serif;font-size:14px;font-weight:500;text-transform:uppercase;line-height:1.3}
.contact-item p{font-size:11px}
.foot-col{top:186px}
.foot-col h6{font-family:"Oswald",sans-serif;font-size:15px;font-weight:500;text-transform:uppercase;letter-spacing:.5px}
.foot-col h6::after{content:"";display:block;width:50px;height:2px;background:var(--red);margin:8px 0 22px}
.foot-about{left:173px;width:220px;font-size:12px;text-align:justify;line-height:1.45}
.foot-social{left:173px;top:398px;display:flex;gap:4px}
.foot-social span{width:20px;height:20px;background:var(--social);display:block}
.foot-links{left:498px;width:260px}
.links{display:grid;grid-template-columns:1fr 1fr;row-gap:6px;font-size:12px;list-style:none}
.links li::before{content:"";display:inline-block;width:5px;height:5px;background:var(--white);margin-right:12px;vertical-align:middle}
.foot-form{left:790px;width:237px}
.field{width:237px;height:34px;background:var(--white);color:#888;font-size:11px;padding:8px 10px;margin-bottom:10px}
.field.msg{height:56px}
.form-btn{width:170px;height:30px;line-height:30px;font-size:13px}
.bottom-bar{top:3997px;height:48px;background:#161616;color:#cfcfcf;font-size:11px;padding:16px 0 0 173px;width:1200px}
</style>
</head>
<body>
<div class="wrap">

<header class="abs site-header wrap">
  <div class="abs logo">BRACKEN LOFT</div>
  <div class="abs top-social" aria-label="Social links"><span></span><span></span><span></span><span></span></div>
  <nav class="abs nav">
    <a class="active" href="#">Home</a><a href="#">About Us</a><a href="#">Services</a><a href="#">Projects</a><a href="#">Contact Us</a>
  </nav>
</header>

<section class="abs hero" role="img" aria-label="Hero slider photo: smiling woman with glasses in a bright office">
  <h1 class="abs hero-title">BRACKEN <span class="accent">LOFT</span></h1>
  <p class="abs hero-sub">Building Software Better</p>
  <span class="abs btn hero-btn">Learn More</span>
  <span class="abs arrow" style="left:18px"><svg width="16" height="16" viewBox="0 0 16 16"><path d="M10 2 L4 8 L10 14" stroke="#fff" stroke-width="2" fill="none"/></svg></span>
  <span class="abs arrow" style="left:1142px"><svg width="16" height="16" viewBox="0 0 16 16"><path d="M6 2 L12 8 L6 14" stroke="#fff" stroke-width="2" fill="none"/></svg></span>
</section>

<section class="abs about wrap">
  <div class="abs about-photo" role="img" aria-label="Red-tinted photo of two colleagues talking"></div>
  <div class="abs about-frame"></div>
  <h2 class="abs head about-title">About to <span class="accent">Bracken Loft</span></h2>
  <h3 class="abs about-sub">Nunc porta turpis at leo posuere convallis</h3>
  <p class="abs about-text">Lorem ipsum dolor sit amet, consectetur adipiscing elit. Fusce aliquet, massa ac ornare feugiat, nunc dui auctor ipsum, sed posuere eros sapien id quam. Lorem ipsum dolor sit amet, consectetur adipiscing elit. Fusce aliquet, massa ac ornare feugiat, nunc dui auctor ipsum, sed posuere eros sapien id quam.</p>
  <ul class="abs checks">
    <li><i></i>Suspendisse aliquam ligula eget odio ornare</li>
    <li><i></i>Fusce aliquet, massa ac ornare feugiat</li>
    <li><i></i>Sed posuere eros sapien id quam</li>
  </ul>
  <span class="abs btn btn-red about-btn">Read More</span>
</section>

<section class="abs services wrap">
  <h2 class="section-title">Our <span class="accent">Services</span></h2>
  <p class="section-intro">Lorem Ipsum is simply dummy text of the printing and typesetting industry. Lorem Ipsum has been the industry's standard Lorem Ipsum is simply dummy text of the printing.</p>
  <div class="abs service-grid">
    <div class="service"><div class="service-icon"><svg width="24" height="24" viewBox="0 0 24 24" fill="none" stroke="#ec1f27" stroke-width="1.6"><rect x="3" y="3" width="7" height="7"/><rect x="14" y="3" width="7" height="7"/><rect x="3" y="14" width="7" height="7"/><rect x="14" y="14" width="7" height="7"/></svg></div><h3>Blockchain Development</h3><p>Consumable and starting materials for API and Intermediate manufacturing or</p></div>
    <div class="service"><div class="service-icon"><svg width="26" height="20" viewBox="0 0 26 20"><path d="M7 18h13a5 5 0 0 0 0-10 7 7 0 0 0-13-1 5.5 5.5 0 0 0 0 11z" fill="#ec1f27"/></svg></div><h3>Cloud Computing</h3><p>Lorem Ipsum is simply dummy text of the printing and typesetting industry.</p></div>
    <div class="service"><div class="service-icon"><svg width="24" height="24" viewBox="0 0 24 24" fill="none" stroke="#ec1f27" stroke-width="1.6"><path d="M12 3v18M3 12h18M6 6l12 12M18 6L6 18"/><circle cx="12" cy="12" r="3" fill="#ec1f27"/></svg></div><h3>Augmented Reality Solutions</h3><p>Lorem Ipsum is simply dummy text of the printing and typesetting industry.!</p></div>
    <div class="service"><div class="service-icon"><svg width="24" height="24" viewBox="0 0 24 24" fill="none" stroke="#ec1f27" stroke-width="1.6"><rect x="3" y="4" width="18" height="14"/><path d="M3 8h18M7 12h10M7 15h6"/></svg></div><h3>Web Development</h3><p>Lorem Ipsum is simply dummy text of the printing and typesetting industry.</p></div>
    <div class="service"><div class="service-icon"><svg width="24" height="24" viewBox="0 0 24 24" fill="none" stroke="#ec1f27" stroke-width="1.6"><rect x="3" y="4" width="18" height="12"/><path d="M9 20h6M12 16v4M9 8l-2 2 2 2M15 8l2 2-2 2"/></svg></div><h3>Software Computing</h3><p>Lorem Ipsum is simply dummy text of the printing and typesetting industry.</p></div>
    <div class="service"><div class="service-icon"><svg width="24" height="24" viewBox="0 0 24 24" fill="none" stroke="#ec1f27" stroke-width="1.6"><rect x="4" y="4" width="16" height="16"/><circle cx="12" cy="12" r="4"/><path d="M12 2v4M12 18v4M2 12h4M18 12h4"/></svg></div><h3>Easy to Customized</h3><p>Lorem Ipsum is simply dummy text of the printing and typesetting industry.</p></div>
  </div>
  <span class="abs btn btn-red services-btn">Read More</span>
</section>

<section class="abs stats wrap">
  <div class="abs stat" style="left:232px"><svg width="26" height="22" viewBox="0 0 26 22" fill="#fff"><rect x="0" y="1" width="4" height="4"/><rect x="7" y="1" width="19" height="4"/><rect x="0" y="9" width="4" height="4"/><rect x="7" y="9" width="19" height="4"/><rect x="0" y="17" width="4" height="4"/><rect x="7" y="17" width="19" height="4"/></svg><strong>25</strong><span>year of experience</span></div>
  <div class="abs stat" style="left:475px"><svg width="34" height="22" viewBox="0 0 34 22" fill="#fff"><circle cx="17" cy="6" r="5"/><path d="M8 22a9 8 0 0 1 18 0z"/><circle cx="7" cy="8" r="3.5"/><circle cx="27" cy="8" r="3.5"/><path d="M0 20a7 6 0 0 1 9-4v4zM34 20a7 6 0 0 0-9-4v4z"/></svg><strong>100+</strong><span>Client</span></div>
  <div class="abs stat" style="left:717px"><svg width="34" height="22" viewBox="0 0 34 22" fill="#fff"><circle cx="17" cy="6" r="5"/><path d="M8 22a9 8 0 0 1 18 0z"/><circle cx="7" cy="8" r="3.5"/><circle cx="27" cy="8" r="3.5"/><path d="M0 20a7 6 0 0 1 9-4v4zM34 20a7 6 0 0 0-9-4v4z"/></svg><strong>1174</strong><span>Happy Customer</span></div>
  <div class="abs stat" style="left:960px"><svg width="24" height="22" viewBox="0 0 24 22" fill="#fff"><path d="M6 0h12v7a6 6 0 0 1-12 0z"/><path d="M6 2H1v3a5 5 0 0 0 5 5M18 2h5v3a5 5 0 0 1-5 5" stroke="#fff" stroke-width="2" fill="none"/><rect x="10" y="13" width="4" height="5"/><rect x="6" y="18" width="12" height="4"/></svg><strong>88</strong><span>Professional Awards</span></div>
</section>

<section class="abs projects wrap">
  <h2 class="section-title">Our <span class="accent">Project</span></h2>
  <p class="section-intro">Lorem Ipsum is simply dummy text of the printing and typesetting industry. Lorem Ipsum has been the industry's standard Lorem Ipsum is simply dummy text of the printing.</p>
  <div class="abs filters"><span class="on">All Projects</span><span>Web</span><span>Branding</span><span>Software</span></div>
  <div class="abs project-grid">
    <div class="shot-1" role="img" aria-label="Project photo: woman with headphones at a laptop"></div>
    <div class="shot-2" role="img" aria-label="Project photo: hands typing on a laptop showing a website"></div>
    <div class="shot-3" role="img" aria-label="Project photo: tablet and phone mockup with hover icons"></div>
    <div class="shot-4" role="img" aria-label="Project photo: laptop on a white desk"></div>
    <div class="shot-5" role="img" aria-label="Project illustration: network of app icons"></div>
    <div class="shot-6" role="img" aria-label="Project illustration: head profile with letters and numbers"></div>
    <div class="shot-7" role="img" aria-label="Project illustration: planning arrows on paper"></div>
    <div class="shot-8" role="img" aria-label="Project photo: tablet showing charts"></div>
  </div>
</section>

<section class="abs team wrap">
  <h2 class="section-title">Our <span class="accent">Team</span></h2>
  <p class="section-intro">Lorem Ipsum is simply dummy text of the printing and typesetting industry. Lorem Ipsum has been the industry's standard Lorem Ipsum is simply dummy text of the printing.</p>
  <div class="abs team-box">
    <div class="member"><div class="avatar" role="img" aria-label="Portrait of Owen Barrett"></div><h4>Owen Barrett</h4><p>Chairman</p><div class="member-social"><span></span><span></span><span></span><span></span></div></div>
    <div class="member"><div class="avatar" role="img" aria-label="Portrait of Miles Carver"></div><h4>Miles Carver</h4><p>CEO</p><div class="member-social"><span></span><span></span><span></span><span></span></div></div>
    <div class="member"><div class="avatar" role="img" aria-label="Portrait of Nina Holt"></div><h4>Nina Holt</h4><p>Project Manager</p><div class="member-social"><span></span><span></span><span></span><span></span></div></div>
    <div class="member"><div class="avatar" role="img" aria-label="Portrait of Pablo Duarte"></div><h4>Pablo Duarte</h4><p>Developer</p><div class="member-social"><span></span><span></span><span></span><span></span></div></div>
  </div>
</section>

<section class="abs testimonials wrap">
  <h2 class="abs head testi-title">Testimonials</h2>
  <div class="abs quote-box">Lorem ipsum dolor sit amet, consectetur adipiscing elit. Fusce aliquet, massa ac ornare feugiat, nunc dui auctor ipsum, sed posuere eros sapien id quam. Lorem ipsum dolor sit amet, consectetur adipiscing elit. Fusce aliquet</div>
  <svg class="abs quote-mark" width="30" height="24" viewBox="0 0 30 24" fill="#fff"><path d="M0 24V13C0 5 4 1 12 0v5c-4 1-6 3-6 7h6v12zM17 24V13c0-8 4-12 12-13v5c-4 1-6 3-6 7h6v12z"/></svg>
  <div class="abs testi-avatar" role="img" aria-label="Portrait of Clara Voss"></div>
  <div class="abs testi-name"><h5>Clara Voss</h5><p>Lorem Ipsum</p></div>
  <div class="abs dots"><span></span><span></span><span></span></div>
</section>

<footer class="abs footer wrap">
  <div class="abs contact-bar">
    <div class="contact-item"><span class="contact-icon"><svg width="20" height="20" viewBox="0 0 24 24" fill="#fff"><path d="M6.6 10.8a15 15 0 0 0 6.6 6.6l2.2-2.2c.3-.3.7-.4 1-.2 1.1.4 2.3.6 3.6.6.6 0 1 .4 1 1V20c0 .6-.4 1-1 1A17 17 0 0 1 3 4c0-.6.4-1 1-1h3.5c.6 0 1 .4 1 1 0 1.3.2 2.5.6 3.6.1.3 0 .7-.2 1z"/></svg></span><div><h6>Phone</h6><p>+(512)555-0148</p></div></div>
    <div class="contact-item"><span class="contact-icon"><svg width="18" height="22" viewBox="0 0 18 24" fill="#fff"><path d="M9 0a9 9 0 0 0-9 9c0 7 9 15 9 15s9-8 9-15a9 9 0 0 0-9-9zm0 12.5A3.5 3.5 0 1 1 9 5.5a3.5 3.5 0 0 1 0 7z"/></svg></span><div><h6>Address</h6><p>42 Harbour Lane, Sydney 2000</p></div></div>
    <div class="contact-item"><span class="contact-icon"><svg width="22" height="16" viewBox="0 0 22 16"><rect width="22" height="16" fill="#fff"/><path d="M1 1l10 8 10-8" stroke="#2a2a2a" stroke-width="1.6" fill="none"/></svg></span><div><h6>Email</h6><p>info@brackenloft.com.au</p></div></div>
  </div>

  <div class="abs foot-col foot-about"><h6>About Us</h6><p>Lorem Ipsum is simply dummy text of the printing and typesetting industry. Lorem Ipsum, Lorem Ipsum is simply dummy text of the printing and typesetting industry. Lorem Ipsum.</p></div>
  <div class="abs foot-social" aria-label="Social links"><span></span><span></span><span></span><span></span></div>

  <div class="abs foot-col foot-links"><h6>Information Links</h6>
    <ul class="links"><li>Home</li><li>iOS Development</li><li>About Us</li><li>App Development</li><li>Services</li><li>Cloud Services</li><li>Projects</li><li>Contact Us</li></ul>
  </div>

  <div class="abs foot-col foot-form"><h6>Tell Us About Your Project</h6>
    <div class="field">Your Name</div>
    <div class="field">Your Mail</div>
    <div class="field msg">Message</div>
    <span class="btn btn-red form-btn">Talk to our team</span>
  </div>
</footer>

<div class="abs bottom-bar">© 2018 Bracken Loft . All Rights Reserved.</div>

</div>
</body>
</html>
```